Group Medical Practice needs stationery, business cards etc. designed

We need stationery designed for a multisite practice that offers primary medical, dental and behavioral healthcare. We would like a design that is consistent for letterhead, business cards, Microsoft Outlook stationery etc. We have attached our new logo design.

Business

```html
<!DOCTYPE html>
<html lang="en">
<head>
<meta charset="utf-8">
<title>Birch Valley Health Services – Stationery</title>
<link href="https://fonts.googleapis.com/css2?family=Crimson+Text:wght@400;600&family=Open+Sans:wght@400;600&display=swap" rel="stylesheet">
<style>
:root{
  --blue:#2a7ff0;
  --green:#8ae51b;
  --ink:#2b2b2b;
  --paper:#ffffff;
  --stage:#e8e5e1;
  --rule:#555;
}
*{box-sizing:border-box;margin:0;padding:0}
html,body{width:1200px;height:540px;overflow:hidden;background:var(--stage)}
body{position:relative;font-family:"Open Sans",sans-serif;color:var(--ink)}
.sheet,.envelope,.card{position:absolute;background:var(--paper);overflow:hidden;box-shadow:0 2px 6px rgba(0,0,0,.25)}
.swoosh{position:absolute;inset:0;width:100%;height:100%}
.brand{position:absolute;font-family:"Crimson Text",serif;font-weight:600;color:var(--blue);line-height:1.05;text-transform:uppercase;letter-spacing:.5px}
.brand small{display:block;font-size:.62em;text-transform:none;letter-spacing:1px}
.brand.on-dark{color:#fff;text-align:center}
.small{font-family:"Crimson Text",serif;font-size:7.5px;color:var(--ink);line-height:1.35}
.contact-list{position:absolute;list-style:none}
.contact-list li{display:flex;align-items:center;gap:4px}
.contact-list li::before{content:"";width:5px;height:5px;border-radius:50%;background:var(--blue)}
.on-blue li::before{background:#fff}
.option-label{position:absolute;font-size:24px;color:#fff;text-shadow:0 0 0 #000;color:#333}

/* letterheads */
.letterhead-1{left:17px;top:34px;width:343px;height:443px}
.letterhead-fax{left:377px;top:34px;width:341px;height:443px}
.address{position:absolute;text-align:right;color:#fff}
.fax-title{position:absolute;left:13px;top:128px;font-size:22px;font-weight:400}
.fax-fields{position:absolute;left:13px;top:172px;width:317px;display:grid;grid-template-columns:175px 1fr;column-gap:12px;row-gap:10px;font-size:6px}
.fax-fields span{border-bottom:1px solid var(--rule);padding-bottom:1px}
.fax-checks{position:absolute;left:13px;top:263px;width:317px;display:flex;justify-content:space-between;font-size:6px}
.fax-checks span{display:flex;align-items:center;gap:4px}
.fax-checks span::before{content:"";width:7px;height:7px;border:1px solid var(--rule)}

/* envelopes */
.envelope-back-green{left:752px;top:28px;width:382px;height:102px}
.envelope-back-blue{left:740px;top:103px;width:382px;height:172px}
.envelope-front{left:804px;top:198px;width:382px;height:173px;background:linear-gradient(#fff,#ececec)}

/* cards */
.card{top:401px;width:141px;height:80px}
.card-front{left:741px}
.card-blue{left:888px;background:var(--blue)}
.card-green{left:1037px;background:var(--green)}
.web{position:absolute;left:0;right:0;text-align:center;font-family:"Crimson Text",serif;font-size:6.5px;font-weight:600}
</style>
</head>
<body>

<!-- Letterhead -->
<section class="sheet letterhead-1">
  <svg class="swoosh" viewBox="0 0 343 443" preserveAspectRatio="none" aria-hidden="true">
    <path d="M0,0H343V318C326,160 210,26 0,4Z" fill="var(--green)"/>
    <path d="M0,0H343V300C320,150 205,28 6,3Z" fill="#fff"/>
    <path d="M20,0H343V292C318,142 210,22 20,0Z" fill="var(--blue)"/>
  </svg>
  <div class="brand" style="left:10px;top:50px;font-size:13px">Birch Valley<small>Health Services</small></div>
  <p class="small address" style="right:20px;top:36px">Street Name, City Name<br>State Zipcode</p>
  <ul class="contact-list small" style="left:10px;top:405px;font-size:6.5px">
    <li>123-456-7890</li><li>123-456-7856</li><li>birchvalleyhs@mail.com</li><li>www.birchvalleyhs.com</li>
  </ul>
</section>
<div class="option-label" style="left:133px;top:482px">Option-1</div>

<!-- Fax sheet -->
<section class="sheet letterhead-fax">
  <svg class="swoosh" viewBox="0 0 341 443" preserveAspectRatio="none" aria-hidden="true">
    <path d="M0,0H341V318C324,160 210,26 0,4Z" fill="var(--green)"/>
    <path d="M0,0H341V300C318,150 205,28 6,3Z" fill="#fff"/>
    <path d="M20,0H341V292C316,142 210,22 20,0Z" fill="var(--blue)"/>
  </svg>
  <div class="brand" style="left:12px;top:55px;font-size:13px">Birch Valley<small>Health Services</small></div>
  <ul class="contact-list small on-blue" style="right:12px;top:14px;color:#fff;font-size:6.5px">
    <li>123-456-7890</li><li>123-456-7856</li><li>birchvalleyhs@mail.com</li><li>www.birchvalleyhs.com</li>
  </ul>
  <h1 class="fax-title">FAX</h1>
  <div class="fax-fields">
    <span>To :</span><span>From :</span>
    <span>Fax :</span><span>Pages :</span>
    <span>Phone :</span><span>Date :</span>
    <span>Re :</span><span>CC :</span>
  </div>
  <div class="fax-checks">
    <span>Urgent</span><span>For Review</span><span>Please Comment</span><span>Please Reply</span><span>Please Recycle</span>
  </div>
  <p class="small" style="position:absolute;left:13px;top:418px">Street Name, City Name<br>State Zipcode</p>
</section>
<div class="option-label" style="left:491px;top:488px">Option-2</div>

<!-- Envelopes -->
<section class="envelope envelope-back-green">
  <svg class="swoosh" viewBox="0 0 382 102" preserveAspectRatio="none" aria-hidden="true">
    <path d="M0,0H382V16L250,70H132L0,16Z" fill="var(--green)"/>
  </svg>
</section>
<section class="envelope envelope-back-blue">
  <svg class="swoosh" viewBox="0 0 382 172" preserveAspectRatio="none" aria-hidden="true">
    <path d="M0,0H382V22L250,82H132L0,22Z" fill="var(--blue)"/>
  </svg>
  <div class="brand on-dark" style="left:0;right:0;top:38px;font-size:11px">Birch Valley<small>Health Services</small></div>
</section>
<section class="envelope envelope-front">
  <svg class="swoosh" viewBox="0 0 382 173" preserveAspectRatio="none" aria-hidden="true">
    <path d="M0,0H382V118C350,50 230,8 0,2Z" fill="var(--green)"/>
    <path d="M0,0H382V110C348,46 230,8 4,1Z" fill="#fff"/>
    <path d="M120,0H382V104C346,42 250,8 120,0Z" fill="var(--blue)"/>
  </svg>
  <div class="brand" style="left:5px;top:34px;font-size:10px">Birch Valley<small>Health Services</small></div>
  <p class="small" style="position:absolute;left:5px;bottom:6px;font-size:6.5px">Street Name, City Name, State Zipcode</p>
  <p class="small" style="position:absolute;right:14px;bottom:6px;font-size:6.5px">www.birchvalleyhs.com</p>
</section>

<!-- Business cards -->
<section class="card card-front">
  <svg class="swoosh" viewBox="0 0 141 80" preserveAspectRatio="none" aria-hidden="true">
    <path d="M0,0H141V48C128,18 80,3 0,1Z" fill="var(--green)"/>
    <path d="M0,0H141V44C126,16 80,3 2,0Z" fill="#fff"/>
    <path d="M40,0H141V40C124,14 90,3 40,0Z" fill="var(--blue)"/>
  </svg>
  <div class="brand" style="left:4px;top:18px;font-size:7.5px">Birch Valley<small>Health Services</small></div>
  <p class="small" style="position:absolute;right:6px;top:6px;color:#fff;text-align:right;font-size:6.5px;line-height:1.1">Your Name<br><span style="font-size:4.5px">Title</span></p>
  <ul class="contact-list small" style="left:4px;top:47px;font-size:4.5px;line-height:1.5">
    <li>123-456-7890</li><li>123-456-7856</li><li>birchvalleyhs@mail.com</li><li>www.birchvalleyhs.com</li>
  </ul>
  <p class="small" style="position:absolute;left:74px;top:63px;font-size:4.5px;line-height:1.3">Street Name, City Name<br>State Zipcode</p>
</section>
<section class="card card-blue">
  <div class="brand on-dark" style="left:0;right:0;top:38px;font-size:10px">Birch Valley<small>Health Services</small></div>
  <p class="web" style="top:62px;color:var(--green)">www.birchvalleyhs.com</p>
</section>
<section class="card card-green">
  <div class="brand on-dark" style="left:0;right:0;top:38px;font-size:10px">Birch Valley<small>Health Services</small></div>
  <p class="web" style="top:62px;color:var(--blue)">www.birchvalleyhs.com</p>
</section>

</body>
</html>
```